New, clean letterhead for law firm in Colorado using recently designed logo.

Professional letterhead for established law firm rebranding. We service high end clientele with mostly family law and personal injury cases. Need source files for future changes. Prefer logo at top, names of members and staff in left margin, contact info in footer.

Target Market(s)

High wealth individuals

Contact Information for Business Card

Need options for traditional and square two sided business cards

Font styles to use
Serif

Colors
0555a3

Requirements
Must have
• Our logo; blue, gray, and white; modern feel.
Should not have
• Images of people

```html
<!DOCTYPE html>
<html lang="en">
<head>
<meta charset="utf-8">
<title>Halvorsen Reede Law, LLC — Letterhead</title>
<link rel="stylesheet" href="https://fonts.googleapis.com/css2?family=Source+Sans+3:wght@400;600&family=Montserrat:wght@400;600&display=swap">
<style>
  :root {
    --brand-blue: #0555a3;
    --ink: #5a5a5a;
    --ink-soft: #8c8c8c;
    --paper: #ffffff;
    --backdrop: #9a9ea7;
  }
  * { margin: 0; padding: 0; box-sizing: border-box; }
  html, body { width: 1200px; height: 898px; overflow: hidden; }
  body {
    background: var(--backdrop);
    font-family: "Source Sans 3", Arial, sans-serif;
  }
  .letterhead {
    position: absolute;
    left: 295px; top: 18px;
    width: 610px; height: 862px;
    background: var(--paper);
    box-shadow: 0 6px 24px rgba(0,0,0,0.18);
  }
  .firm-name {
    position: absolute;
    top: 104px; left: 0; width: 100%;
    text-align: center;
    font-size: 17px;
    font-weight: 600;
    letter-spacing: 1.5px;
    color: var(--brand-blue);
  }
  .team {
    position: absolute;
    left: 58px; top: 200px;
    width: 118px;
  }
  .team-group { border-top: 1.5px solid var(--brand-blue); padding-top: 14px; margin-bottom: 18px; }
  .member { margin-bottom: 13px; font-size: 9.5px; line-height: 1.25; color: var(--ink-soft); }
  .letter-body {
    position: absolute;
    left: 206px; top: 212px;
    width: 348px;
    color: var(--ink);
    font-size: 11px;
    line-height: 15px;
  }
  .salutation { font-weight: 600; font-size: 11.5px; margin-bottom: 18px; color: #4a4a4a; }
  .letter-body p { margin-bottom: 24px; }
  .page-footer {
    position: absolute;
    left: 58px; right: 40px; bottom: 40px;
    display: flex; align-items: center; justify-content: space-between;
    font-family: "Montserrat", Arial, sans-serif;
    font-size: 8.5px; line-height: 1.45;
    color: var(--ink-soft);
  }
  .page-footer .label { color: var(--brand-blue); font-weight: 600; }
  .divider { width: 1.5px; height: 24px; background: var(--brand-blue); }
  .web { text-align: right; }
</style>
</head>
<body>
  <main class="letterhead">
    <div class="firm-name">HALVORSEN REEDE LAW, LLC</div>

    <aside class="team">
      <div class="team-group">
        <div class="member">Marion LECLERC<br>Avocat Associé</div>
        <div class="member">Sophie DARNELL VAUX<br>Avocat Associé</div>
        <div class="member">Alice MOREAU<br>Avocat Collaborateur</div>
      </div>
      <div class="team-group">
        <div class="member">Marion LECLERC<br>Avocat Associé</div>
        <div class="member">Sophie DARNELL VAUX<br>Avocat Associé</div>
        <div class="member">Alice MOREAU<br>Avocat Collaborateur</div>
      </div>
    </aside>

    <article class="letter-body">
      <div class="salutation">Lorem Ipsum,</div>
      <p>Cras mattis consectetur purus sit amet fermentum. Etiam porta sem malesuada magna mollis euismod. Integer posuere erat a ante venenatis dapibus posuere velit aliquet. Cras justo odio, dapibus ac facilisis in, egestas eget quam. Aenean eu leo quam. Pellentesque ornare sem lacinia quam venenatis vestibulum.</p>
      <p>Vivamus sagittis lacus vel augue laoreet rutrum faucibus dolor auctor. Donec sed odio dui. Etiam porta sem malesuada magna mollis euismod. Morbi leo risus, porta ac consectetur ac, vestibulum at eros. Nullam id dolor id nibh ultricies vehicula ut id elit.</p>
      <p>Cras mattis consectetur purus sit amet fermentum. Etiam porta sem malesuada magna mollis euismod. Integer posuere erat a ante venenatis dapibus posuere velit aliquet. Cras justo odio, dapibus ac facilisis in, egestas eget quam. Aenean eu leo quam. Pellentesque ornare sem lacinia quam venenatis vestibulum.</p>
      <p>Vivamus sagittis lacus vel augue laoreet rutrum faucibus dolor auctor. Donec sed odio dui. Etiam porta sem malesuada magna mollis euismod. Morbi leo risus, porta ac consectetur ac, vestibulum at eros. Nullam id dolor id nibh ultricies vehicula ut id elit.</p>
      <p>Vivamus sagittis lacus vel augue laoreet rutrum faucibus dolor auctor. Donec sed odio dui. Etiam porta sem malesuada magna mollis euismod. Morbi leo risus, porta ac consectetur ac, vestibulum at eros. Nullam id dolor id nibh ultricies vehicula ut id elit.</p>
    </article>

    <footer class="page-footer">
      <div class="phones"><span class="label">Telefon:</span> (303) 555-0142<br><span class="label">Fax:</span> (303) 555-0143</div>
      <div class="divider"></div>
      <div class="address">880 Larkspur Court 3B<br>Boulder, CO 80302</div>
      <div class="divider"></div>
      <div class="web">info@halvorsen-reede.com<br>www.halvorsen-reede.com</div>
    </footer>
  </main>
</body>
</html>
```